PowerPoint template for large technology company

Requesting proposals for a PowerPoint deck template that can be used by our sales team when pitching clients. We are a large technology media company, that is BtoB focused, and are looking for a professional, clean, tech-forward, design and layout. However, our clients are advertisers and brands who would respond well to a subtly stylized creative design.

We need a fully built-out template wherein our sales team can choose from a variety of slide layouts while compiling their pitch decks.

Key objective: To create a template that mandates consistent fonts, sizes, and layout, and is easy to use for novice presenters. A plug-and-play template.

Secondary objective: A refresh on current design of company template.

Presentation template should include:
2 Presentation title slide options
2 Section header options
6 information layout slide options
3 data charts (pie, bar, and column)
Summary/ Thank you slide

The teams using this template will not be adept with PowerPoint but should easily be able to insert images and text boxes without it ruining the design and format of the presentation. The idea is if 20 people use our template to build pitch-decks, all of the individual decks should all look like they came from the same team. Please be as detailed and specific as possible when building out slides.

Simple, high-compatibility fonts. Please see brand guidelines attached.

Target Market(s)

Large advertising agencies and major consumer technology brands.

This deck template will not be consumer facing.

Industry/Entity Type

Building

Font styles to use
Serif
Sans Serif

Requirements
Must have
• Must be clean, high-tech, and forces user to stay within template guidelines during modifications.

Template should be built out for a sales presentation that will be a tool for ppt novices.
Nice to have
• As we are revamping existing decks, it will be nice to see multiple ideas on the design. Think professional, high-tech, and powerful.
Should not have
• Should not have a distracting background that will interfere with presentations or where it will be difficult to easily insert images.

Blacked out backgrounds cause a "boxed in" look for images and/or text boxes - which is undesirable. Either don't include color-blocked backgrounds or introduce a way in which this can be used that avoids the previously stated pitfall.

No rotated text-fill options. (i.e. rotating text by 90 or 180 degrees)

Please don't be too literal in your design approach.

```html
<!DOCTYPE html>
<html lang="en">
<head>
<meta charset="utf-8">
<title>Northwave Sales Deck Template</title>
<link href="https://fonts.googleapis.com/css2?family=Open+Sans:wght@400;600;700&display=swap" rel="stylesheet">
<style>
  :root {
    --page: #0b0b0b;
    --blue-deep: #1f5fa8;
    --blue-mid: #3a7cc4;
    --blue-light: #8fbbe6;
    --blue-pale: #dbe9f6;
    --title-blue: #5b8fc6;
    --lime: #d7e64a;
    --ink: #3d3d3d;
    --ink-soft: #707070;
    --white: #ffffff;
    --navy: #15345e;
  }
  * { box-sizing: border-box; margin: 0; padding: 0; }
  html, body { width: 1053px; height: 1200px; overflow: hidden; background: var(--page); }
  body { font-family: "Open Sans", Arial, sans-serif; color: var(--ink); }

  .deck {
    position: relative; width: 1053px; height: 1200px;
    display: grid;
    grid-template-columns: 360px 360px;
    grid-template-rows: repeat(4, 270px);
    column-gap: 80px; row-gap: 24px;
    padding: 24px 146px;
  }
  .slide {
    position: relative; width: 360px; height: 270px; overflow: hidden;
    background: var(--white);
    box-shadow: 0 2px 8px rgba(0,0,0,.5);
  }
  .slide svg.bg { position: absolute; inset: 0; width: 100%; height: 100%; }

  .slide-head { position: absolute; top: 16px; left: 20px; display: flex; align-items: center; gap: 6px; }
  .slide-head .mark { width: 13px; height: 13px; border-radius: 50%; background: radial-gradient(circle at 35% 35%, var(--blue-light), var(--blue-deep)); flex: none; }
  .slide-head h2 { font-size: 10px; font-weight: 400; color: var(--title-blue); line-height: 1.15; }
  .foot-brand { position: absolute; left: 22px; bottom: 16px; }
  .brand-name { font-weight: 600; color: var(--blue-mid); line-height: 1; }
  .foot-brand .brand-name { font-size: 9px; }
  .foot-brand .tagline { font-size: 4px; color: var(--ink-soft); }
  .foot-url { position: absolute; left: 150px; bottom: 19px; font-size: 4.5px; color: var(--ink-soft); }
  .body-copy { font-size: 4.6px; line-height: 1.45; color: var(--ink); }
  .body-copy p + p { margin-top: 4px; }

  .placeholder { position: absolute; }

  .cover .url-top { position: absolute; top: 38px; left: 120px; font-size: 4.5px; color: var(--white); opacity: .85; }
  .cover .brand-block { position: absolute; left: 105px; top: 135px; }
  .cover .brand-block .brand-name { font-size: 24px; font-weight: 400; color: #5c6b7a; }
  .cover .brand-block .tagline { font-size: 6px; color: var(--blue-mid); margin-left: 30px; margin-top: 2px; }
  .cover .address { position: absolute; right: 20px; bottom: 18px; text-align: right; font-size: 3.8px; line-height: 1.4; color: var(--ink-soft); }
  .cover .address strong { color: var(--blue-mid); font-weight: 600; }

  .title-slide { background: var(--blue-deep); }
  .hero-title { position: absolute; left: 0; right: 0; text-align: center; color: var(--white); font-size: 16px; font-weight: 400; }
  .hero-sub { position: absolute; left: 0; right: 0; text-align: center; color: var(--lime); font-size: 5px; font-weight: 700; letter-spacing: .3px; }
  .title-slide .hero-title { top: 100px; }
  .title-slide .hero-sub { top: 123px; }
  .title-slide .brand-light { position: absolute; left: 26px; bottom: 26px; color: var(--white); }
  .title-slide .brand-light .brand-name { color: var(--white); font-size: 11px; }
  .title-slide .brand-light .tagline { font-size: 4.5px; margin-left: 14px; }
  .presenter { position: absolute; right: 26px; bottom: 22px; display: flex; align-items: flex-end; gap: 5px; }
  .presenter .meta { font-size: 3.8px; color: var(--white); text-align: right; line-height: 1.4; }
  .presenter .photo { position: relative; width: 26px; height: 32px; background: linear-gradient(#c9d3dc, #7d8a96); border: 1px solid var(--white); }

  .divider .url-top { position: absolute; top: 14px; left: 0; right: 0; text-align: center; font-size: 4.5px; color: var(--white); opacity: .85; }
  .divider .hero-title { top: 98px; font-weight: 600; }
  .divider .hero-sub { top: 120px; }
  .divider .brand-right { position: absolute; right: 40px; bottom: 26px; }
  .divider .brand-right .brand-name { font-size: 11px; color: #5c6b7a; font-weight: 400; }
  .divider .brand-right .tagline { font-size: 4px; color: var(--ink-soft); margin-left: 14px; }
  .divider .page-no { position: absolute; right: 22px; bottom: 30px; font-size: 5px; color: var(--ink-soft); }

  .s-image-text .photo { left: 46px; top: 48px; width: 76px; height: 100px; background: linear-gradient(#2c3e63, #6d7f9c 60%, #c5a970); }
  .s-image-text .body-copy { position: absolute; left: 182px; top: 48px; width: 140px; }

  .points { position: absolute; top: 52px; left: 40px; right: 26px; display: grid; grid-template-columns: 1fr 1fr; column-gap: 20px; }
  .point { display: flex; gap: 7px; margin-bottom: 10px; }
  .point .dot { width: 12px; height: 12px; border-radius: 50%; background: var(--blue-pale); border: 1px solid var(--blue-light); flex: none; display: flex; align-items: center; justify-content: center; font-size: 4px; color: var(--blue-deep); margin-top: 4px; }
  .point h3 { font-size: 5px; font-weight: 700; color: var(--ink); margin-bottom: 1px; }
  .point p { font-size: 4.3px; line-height: 1.4; color: var(--ink); }

  .s-map .slide-head h2 { width: 150px; }
  .s-map .map { left: 55px; top: 68px; width: 250px; height: 130px; background: radial-gradient(ellipse at center, #c6cdd6 0%, #dfe3e8 65%, var(--white) 100%); border-radius: 40%; }

  .team { position: absolute; top: 58px; left: 38px; right: 38px; display: flex; justify-content: space-between; }
  .member { width: 82px; text-align: center; }
  .member .face { position: relative; width: 44px; height: 44px; border-radius: 50%; margin: 0 auto 5px; border: 2px solid var(--white); box-shadow: 0 1px 3px rgba(0,0,0,.25); }
  .member:nth-child(1) .face { background: linear-gradient(#d8cfc5, #8c7a6a); }
  .member:nth-child(2) .face { background: linear-gradient(#e7ece2, #a9b6a2); }
  .member:nth-child(3) .face { background: linear-gradient(#e8e6e2, #b7a79a); }
  .member h3 { font-size: 4.6px; font-weight: 700; }
  .member p { font-size: 4px; line-height: 1.4; color: var(--ink); }

  .s-chart .body-copy { position: absolute; left: 26px; top: 48px; width: 116px; }
  .s-chart .chart { position: absolute; left: 178px; top: 64px; width: 150px; height: 90px; }
  .legend { position: absolute; left: 190px; top: 158px; display: flex; gap: 9px; font-size: 3.8px; color: var(--ink-soft); }
</style>
</head>
<body>
<main class="deck">

  <section class="slide cover">
    <svg class="bg" viewBox="0 0 360 270" preserveAspectRatio="none" aria-hidden="true">
      <defs>
        <linearGradient id="coverBlue" x1="0" y1="0" x2="0" y2="1">
          <stop offset="0" stop-color="#2f73bf"/><stop offset="1" stop-color="#8fbbe6"/>
        </linearGradient>
        <linearGradient id="coverFloor" x1="0" y1="0" x2="0" y2="1">
          <stop offset="0" stop-color="#ffffff"/><stop offset="1" stop-color="#eef3f8"/>
        </linearGradient>
      </defs>
      <rect width="360" height="270" fill="url(#coverFloor)"/>
      <path d="M0 0H360V140C280 110 90 100 0 150Z" fill="url(#coverBlue)"/>
      <path d="M0 150C90 100 280 110 360 140" fill="none" stroke="#dbe9f6" stroke-width="2"/>
    </svg>
    <div class="url-top">www.northwave-media.com</div>
    <div class="brand-block">
      <div class="brand-name">Northwave</div>
      <div class="tagline">Insight Driven Media</div>
    </div>
    <div class="address">
      <strong>Northwave Media Headquarters</strong><br>
      400 Harbor Way, Suite 12<br>
      San Mateo, CA 94400 · 555 010 2040
    </div>
  </section>

  <section class="slide title-slide">
    <svg class="bg" viewBox="0 0 360 270" preserveAspectRatio="none" aria-hidden="true">
      <defs>
        <linearGradient id="titleBlue" x1="0" y1="0" x2="0" y2="1">
          <stop offset="0" stop-color="#3f86cf"/><stop offset="1" stop-color="#1b559b"/>
        </linearGradient>
      </defs>
      <rect width="360" height="270" fill="url(#titleBlue)"/>
      <path d="M0 0H360V60C250 35 110 45 0 80Z" fill="#6aa6de" opacity=".55"/>
      <path d="M0 80C110 45 250 35 360 60" fill="none" stroke="#ffffff" stroke-width="1.5" opacity=".8"/>
    </svg>
    <h1 class="hero-title">Presentation Tittle Here</h1>
    <div class="hero-sub">YOUR PRESENTATION SUB TITLE HERE</div>
    <div class="brand-light">
      <div class="brand-name">Northwave</div>
      <div class="tagline">Insight Driven Media</div>
    </div>
    <div class="presenter">
      <div class="meta">Presenter Name<br>Account Director</div>
      <div class="photo" role="img" aria-label="Presenter portrait photo"></div>
    </div>
  </section>

  <section class="slide s-image-text">
    <svg class="bg" viewBox="0 0 360 270" preserveAspectRatio="none" aria-hidden="true">
      <path d="M140 270C220 262 300 250 360 222V270Z" fill="#3a7cc4"/>
      <path d="M110 270C210 258 300 244 360 212" fill="none" stroke="#8fbbe6" stroke-width="1.5"/>
    </svg>
    <header class="slide-head"><span class="mark"></span><h2>Northwave Slide Presentation 1</h2></header>
    <div class="placeholder photo" role="img" aria-label="Photo of a glass office tower at night"></div>
    <div class="body-copy">
      <p>Our team has forged a bold and dynamic approach to the way brands reach technology buyers. By combining audience data with premium content, we help advertisers connect with the decision makers who matter most to their growth.</p>
      <p>Building on this approach, we partner with leading agencies to plan campaigns that reach a new level of precision and impact, supported by clear reporting and measurable results across every channel we manage.</p>
      <p>The pace at which insight turns into action has never been faster for our clients.</p>
    </div>
    <div class="foot-brand"><div class="brand-name">Northwave</div><div class="tagline">Insight Driven Media</div></div>
    <div class="foot-url">www.northwave-media.com</div>
  </section>

  <section class="slide s-points">
    <svg class="bg" viewBox="0 0 360 270" preserveAspectRatio="none" aria-hidden="true">
      <path d="M140 270C220 262 300 250 360 222V270Z" fill="#3a7cc4"/>
      <path d="M110 270C210 258 300 244 360 212" fill="none" stroke="#8fbbe6" stroke-width="1.5"/>
    </svg>
    <header class="slide-head"><span class="mark"></span><h2>Northwave Slide Presentation 4</h2></header>
    <div class="points">
      <div>
        <div class="point"><span class="dot">1</span><div><h3>Service Point 1</h3><p>Short supporting copy that explains this point in one or two lines of text.</p></div></div>
        <div class="point"><span class="dot">2</span><div><h3>Service Point 2</h3><p>Short supporting copy that explains this point in one line.</p></div></div>
        <div class="point"><span class="dot">3</span><div><h3>Service Point 3</h3><p>Short supporting copy that explains this point clearly.</p></div></div>
      </div>
      <div>
        <div class="point"><span class="dot">4</span><div><h3>Service Point 4</h3><p>Short supporting copy that explains this point in one or two lines of text.</p></div></div>
        <div class="point"><span class="dot">5</span><div><h3>Service Point 5</h3><p>Short supporting copy that explains this point in one or two lines of text for the reader.</p></div></div>
      </div>
    </div>
    <div class="foot-brand"><div class="brand-name">Northwave</div><div class="tagline">Insight Driven Media</div></div>
    <div class="foot-url">www.northwave-media.com</div>
  </section>

  <section class="slide s-map">
    <svg class="bg" viewBox="0 0 360 270" preserveAspectRatio="none" aria-hidden="true">
      <path d="M140 270C220 262 300 250 360 222V270Z" fill="#3a7cc4"/>
      <path d="M110 270C210 258 300 244 360 212" fill="none" stroke="#8fbbe6" stroke-width="1.5"/>
    </svg>
    <header class="slide-head"><span class="mark"></span><h2>More Than 500+ Satisfied Client Over All the World</h2></header>
    <div class="placeholder map" role="img" aria-label="Grey world map with client location markers"></div>
    <div class="foot-brand"><div class="brand-name">Northwave</div><div class="tagline">Insight Driven Media</div></div>
    <div class="foot-url">www.northwave-media.com</div>
  </section>

  <section class="slide divider">
    <svg class="bg" viewBox="0 0 360 270" preserveAspectRatio="none" aria-hidden="true">
      <defs>
        <linearGradient id="divBlue" x1="0" y1="0" x2="0" y2="1">
          <stop offset="0" stop-color="#2f73bf"/><stop offset="1" stop-color="#5e9ad6"/>
        </linearGradient>
      </defs>
      <rect width="360" height="270" fill="#f3f6fa"/>
      <path d="M0 0H360V190C270 160 90 165 0 210Z" fill="url(#divBlue)"/>
      <path d="M0 210C90 165 270 160 360 190" fill="none" stroke="#dbe9f6" stroke-width="2"/>
    </svg>
    <div class="url-top">www.northwave-media.com</div>
    <h1 class="hero-title">Divider Pages Here</h1>
    <div class="hero-sub">PRESENTATION SUB TITLE HERE</div>
    <div class="brand-right"><div class="brand-name">Northwave</div><div class="tagline">Insight Driven Media</div></div>
    <div class="page-no">7</div>
  </section>

  <section class="slide s-team">
    <svg class="bg" viewBox="0 0 360 270" preserveAspectRatio="none" aria-hidden="true">
      <path d="M140 270C220 262 300 250 360 222V270Z" fill="#3a7cc4"/>
      <path d="M110 270C210 258 300 244 360 212" fill="none" stroke="#8fbbe6" stroke-width="1.5"/>
    </svg>
    <header class="slide-head"><span class="mark"></span><h2>Northwave Slide Presentation 5</h2></header>
    <div class="team">
      <div class="member"><div class="face" role="img" aria-label="Portrait photo of a team member"></div><h3>Team Member One</h3><p>Short description of this role and the value it brings to each client.</p></div>
      <div class="member"><div class="face" role="img" aria-label="Photo of a product detail"></div><h3>Team Member Two</h3><p>Short description of this role and the value it brings to each client.</p></div>
      <div class="member"><div class="face" role="img" aria-label="Portrait photo of a support specialist"></div><h3>Team Member Three</h3><p>Short description of this role and the value it brings to each client.</p></div>
    </div>
    <div class="foot-brand"><div class="brand-name">Northwave</div><div class="tagline">Insight Driven Media</div></div>
    <div class="foot-url">www.northwave-media.com</div>
  </section>

  <section class="slide s-chart">
    <svg class="bg" viewBox="0 0 360 270" preserveAspectRatio="none" aria-hidden="true">
      <path d="M140 270C220 262 300 250 360 222V270Z" fill="#3a7cc4"/>
      <path d="M110 270C210 258 300 244 360 212" fill="none" stroke="#8fbbe6" stroke-width="1.5"/>
    </svg>
    <header class="slide-head"><span class="mark"></span><h2>Northwave Slide Presentation 8</h2></header>
    <div class="body-copy">
      <p>Our team has forged a bold and dynamic approach to reaching technology buyers. By combining audience data with premium content, we help advertisers connect with decision makers.</p>
      <p>Building on this approach, we partner with leading agencies to plan campaigns with new precision, supported by clear reporting and measurable results across every channel we manage for our clients.</p>
    </div>
    <svg class="chart" viewBox="0 0 150 90" aria-label="Pie chart with four segments">
      <path d="M75 45L75 5A40 40 0 1 1 38 60Z" fill="#3a7cc4"/>
      <path d="M75 45L38 60A40 40 0 0 1 40 25Z" fill="#c8ccd1"/>
      <path d="M75 45L40 25A40 40 0 0 1 58 9Z" fill="#8a8f96"/>
      <path d="M75 45L58 9A40 40 0 0 1 75 5Z" fill="#15345e"/>
    </svg>
    <div class="legend"><span>Product</span><span>Product</span><span>Product</span><span>Product</span></div>
    <div class="foot-brand"><div class="brand-name">Northwave</div><div class="tagline">Insight Driven Media</div></div>
    <div class="foot-url">www.northwave-media.com</div>
  </section>

</main>
</body>
</html>
```